Lantern Hearthworks Business Cards

Looking to create simple business cards that highlight our unique three sided triangle fire pit design with the colors and font of our logo, listed below.

Requirements
Must have
• Looking for something simple that includes a picture of our fire pit with name, website (lanternhearthworks.com), phone number and email. Want to keep the color mostly orange and black.
• Font is gotham(medium) and orange color code is #ee6e22

```html
<!DOCTYPE html>
<html lang="en">
<head>
<meta charset="UTF-8">
<title>Lantern Hearthworks Business Cards</title>
<link href="https://fonts.googleapis.com/css2?family=Montserrat:wght@400;500;600&display=swap" rel="stylesheet">
<style>
  :root {
    --orange: #ee6e22;
    --black: #141414;
    --ink: #2b2b2b;
    --grey: #5a5a5a;
    --white: #ffffff;
    --backdrop: #2a2a2a;
  }
  * { margin: 0; padding: 0; box-sizing: border-box; }
  html, body { width: 1200px; height: 901px; overflow: hidden; }
  body {
    background: var(--backdrop);
    font-family: "Montserrat", Arial, sans-serif;
    position: relative;
  }
  .card {
    position: absolute;
    left: 270px;
    width: 660px;
    height: 377px;
    overflow: hidden;
    box-shadow: 0 10px 30px rgba(0,0,0,.45);
  }
  .card-front { top: 60px; background: var(--black); border-bottom: 6px solid var(--orange); }
  .card-back { top: 477px; background: var(--white); border-bottom: 6px solid var(--orange); }

  .fire-photo {
    position: absolute; left: 0; top: 0; width: 100%; height: 100%;
    background:
      linear-gradient(90deg, rgba(20,20,20,0) 45%, var(--black) 72%),
      radial-gradient(ellipse at 30% 35%, #ffb23a 0%, #f07a1c 30%, #a9400c 55%, #3a1a0a 80%);
  }

  .brand {
    position: absolute;
    display: flex; align-items: center; gap: 14px;
  }
  .brand-mark { width: 14px; height: 14px; flex: none; }
  .brand-divider { width: 1px; flex: none; }
  .brand-name {
    font-weight: 500;
    letter-spacing: 5px;
    line-height: 1.15;
    text-transform: uppercase;
    white-space: nowrap;
  }
  .card-front .brand { right: 40px; bottom: 40px; }
  .card-front .brand-mark { background: var(--white); }
  .card-front .brand-divider { background: var(--white); height: 96px; }
  .card-front .brand-name { color: var(--white); font-size: 26px; }

  .card-back .brand { left: 36px; top: 150px; }
  .card-back .brand-mark { background: var(--orange); }
  .card-back .brand-divider { background: #9a9a9a; height: 80px; }
  .card-back .brand-name { color: var(--orange); font-size: 18px; letter-spacing: 4px; }

  .rule { position: absolute; left: 318px; top: 120px; width: 2px; height: 140px; background: var(--ink); }

  .contact { position: absolute; left: 346px; top: 118px; color: var(--ink); white-space: nowrap; }
  .contact-name { color: var(--orange); font-size: 26px; font-weight: 600; line-height: 1.1; }
  .contact-role { font-size: 15px; font-weight: 400; margin-bottom: 18px; }
  .contact-line { display: flex; align-items: center; gap: 11px; font-size: 15px; margin-bottom: 9px; }
  .contact-line svg { width: 13px; height: 13px; flex: none; }
</style>
</head>
<body>
  <section class="card card-front">
    <div class="fire-photo" role="img" aria-label="Photo of flames rising from a triangular glass-lined fire pit"></div>
    <div class="brand">
      <span class="brand-mark"></span>
      <span class="brand-divider"></span>
      <span class="brand-name">Lantern<br>Hearthworks</span>
    </div>
  </section>

  <section class="card card-back">
    <div class="brand">
      <span class="brand-mark"></span>
      <span class="brand-divider"></span>
      <span class="brand-name">Lantern<br>Hearthworks</span>
    </div>
    <div class="rule"></div>
    <div class="contact">
      <p class="contact-name">Elias Marrow</p>
      <p class="contact-role">Co Founder</p>
      <p class="contact-line">
        <svg viewBox="0 0 24 24"><path fill="#ee6e22" d="M6.6 10.8a15 15 0 0 0 6.6 6.6l2.2-2.2a1 1 0 0 1 1-.25 11.4 11.4 0 0 0 3.6.57 1 1 0 0 1 1 1V20a1 1 0 0 1-1 1A17 17 0 0 1 3 4a1 1 0 0 1 1-1h3.5a1 1 0 0 1 1 1c0 1.25.2 2.45.57 3.570a1 1 0 0 1-.25 1z"/></svg>
        503-555-0147
      </p>
      <p class="contact-line">
        <svg viewBox="0 0 24 24"><path fill="#ee6e22" d="M2 5h20v14H2z"/><path fill="none" stroke="#fff" stroke-width="1.6" d="M2.5 5.5 12 13l9.5-7.5"/></svg>
        hello@lanternhearthworks.com
      </p>
      <p class="contact-line">
        <svg viewBox="0 0 24 24"><circle cx="12" cy="12" r="10" fill="#ee6e22"/><circle cx="12" cy="12" r="4" fill="#fff"/></svg>
        www.lanternhearthworks.com
      </p>
    </div>
  </section>
</body>
</html>
```